Bright Tutor Hub business card

Use existing logo to design a business card which contains information that is listed below. Use of logo as attached. It is important that the colour scheme matches the logo already designed. It needs to be crisp and professional. This is an on line business, a database of training providers for educational establishments. The website will provide users with full information on trainers who are available and their credibility.
Target Market(s)
Educators and training providers
Industry/Entity Type
Education
Contact Information for Business Card
Font styles to use
Colors
Designer to choose colors to be used in the design.
Requirements
Must have
- Email address mara@brighttutorhub.co.uk
- Twitter feed. @MaraBth
- LinkedIn details Mara Fenwick
- Mobile phone number 07812 459302
- Mission statement: To create a learning network that ensures that schools receive first class training that is excellent value for money.
Nice to have
- N/a
Should not have
- Twee educational images

```html
<!DOCTYPE html>
<html lang="en">
<head>
<meta charset="utf-8">
<title>Bright Tutor Hub business card</title>
<link rel="stylesheet" href="https://fonts.googleapis.com/css2?family=Montserrat:wght@500;600&family=Open+Sans:wght@400;600&display=swap">
<style>
  :root {
    --page: #e9ecef;
    --card-white: #ffffff;
    --brand-blue: #1f78c1;
    --brand-deep: #2a74b8;
    --brand-light: #39a9da;
    --ink: #1b1b1b;
    --on-blue: #ffffff;
    --rule: rgba(20, 70, 130, 0.55);
  }
  * { box-sizing: border-box; margin: 0; padding: 0; }
  html, body {
    width: 1200px; height: 1000px; overflow: hidden;
    background: var(--page);
  }
  .canvas { position: relative; width: 1200px; height: 1000px; }
  .card {
    position: absolute; width: 640px; height: 380px;
    border-radius: 26px;
    box-shadow: 0 10px 30px rgba(0,0,0,0.18);
    overflow: hidden;
  }
  .card--contact { left: 80px; top: 80px; background: var(--card-white); }
  .card--mission {
    left: 480px; top: 540px;
    background: linear-gradient(160deg, var(--brand-deep) 0%, var(--brand-light) 100%);
    color: var(--on-blue);
  }
  .brand-name {
    font-family: "Montserrat", sans-serif;
    font-weight: 600;
    letter-spacing: 1px;
    text-transform: uppercase;
    display: flex; align-items: center; gap: 14px;
    position: absolute;
  }
  .brand-mark { border-radius: 50%; flex: none; }
  .card--contact .brand-name {
    color: var(--brand-blue); font-size: 38px;
    left: 150px; top: 70px;
  }
  .card--contact .brand-mark { width: 34px; height: 34px; background: var(--brand-blue); }
  .contact-list {
    position: absolute; left: 40px; bottom: 34px;
    font-family: "Open Sans", sans-serif; font-size: 17px; line-height: 1.6;
    color: var(--ink); list-style: none;
  }
  .contact-list .label { color: var(--brand-blue); }
  .contact-list .sep { color: var(--ink); margin: 0 6px; }
  .contact-list .gap { margin-left: 40px; }
  .card--mission .brand-name {
    color: var(--on-blue); font-size: 42px;
    left: 0; right: 0; justify-content: center; top: 90px;
  }
  .card--mission .brand-mark { width: 38px; height: 38px; background: var(--on-blue); }
  .mission-rule {
    position: absolute; left: 140px; right: 140px; height: 2px;
    background: var(--rule);
  }
  .mission-rule--top { top: 222px; }
  .mission-rule--bottom { top: 318px; }
  .mission-statement {
    position: absolute; left: 70px; right: 70px; top: 240px;
    font-family: "Open Sans", sans-serif; font-size: 17px; line-height: 1.5;
    text-align: center;
  }
</style>
</head>
<body>
<main class="canvas">
  <section class="card card--contact" aria-label="Business card front">
    <div class="brand-name"><span class="brand-mark"></span>Bright Tutor Hub</div>
    <ul class="contact-list">
      <li><span class="label">Mobile:</span> 07812 459302<span class="sep">|</span><span class="label">Email:</span> mara@brighttutorhub.co.uk</li>
      <li><span class="label">Twitter</span>@MaraBth<span class="gap"></span><span class="label">LinkedIn</span> Mara Fenwick</li>
    </ul>
  </section>

  <section class="card card--mission" aria-label="Business card back">
    <div class="brand-name"><span class="brand-mark"></span>Bright Tutor Hub</div>
    <div class="mission-rule mission-rule--top"></div>
    <p class="mission-statement">To create a learning network that ensures that schools receive first class training that is excellent value for money.</p>
    <div class="mission-rule mission-rule--bottom"></div>
  </section>
</main>
</body>
</html>
```